This 3D poster will be our launch poster on Facebook which we use for the social media promotions.

We help students connect with apartments and utilities. We have a logo which represents that. Now, we are launching our Facebook page. So, I am looking for a Facebook cover photo. This photo is nothing but a 3D poster. We want it to convey the below information in most artistic manner to students (our target audience).
Information:
Student (joining university) , Apartment + Electricity + Internet + Mobile connection = Bright Nestwell.
Unpack by dawn (our tag line).

Attached is the logo for your reference. We want it to be very attractive but with not more than 150 words of information.

Target Market(s)

Students

Industry/Entity Type

Online

Font styles to use
Script

Colors

Designer to choose colors to be used in the design.

Requirements
Must have
• 3D Design, Very good color combination, Our company logo
Nice to have
• Divide our logo into 5 parts like man, house, electricity, internet, sim card and then try to combine them and design our logo in an artistic manner. This should represent our story. But, its up to you to follow this
Should not have
• More than 150 words

```html
<!DOCTYPE html>
<html lang="en">
<head>
<meta charset="utf-8">
<title>Bright Nestwell – Launch Cover</title>
<link href="https://fonts.googleapis.com/css2?family=Tinos:wght@700&display=swap" rel="stylesheet">
<style>
  :root {
    --accent: #f08c00;
    --ink: #111111;
    --screen: #ececec;
    --bulb: #2a2ab0;
    --socket: #1d6fb8;
    --bg-top: #b9b9b9;
    --bg-mid: #c6c6c6;
    --bg-bottom: #f0f0f0;
  }
  html, body {
    margin: 0;
    padding: 0;
    overflow: hidden;
  }
  .cover {
    position: relative;
    width: 1200px;
    height: 961px;
    overflow: hidden;
    background:
      radial-gradient(ellipse 70% 40% at 85% 5%, rgba(150,150,150,0.55), rgba(150,150,150,0) 70%),
      linear-gradient(180deg, var(--bg-top) 0%, var(--bg-mid) 55%, var(--bg-bottom) 100%);
    font-family: "Tinos", "Times New Roman", serif;
  }
  .floor-shadow {
    position: absolute;
    left: 0;
    top: 596px;
    width: 1200px;
    height: 14px;
    background: radial-gradient(ellipse 50% 50% at 50% 50%, rgba(0,0,0,0.12), rgba(0,0,0,0) 100%);
  }
  .web-address, .hashtag {
    position: absolute;
    margin: 0;
    color: var(--accent);
    font-weight: 700;
    white-space: nowrap;
    line-height: 1;
  }
  .web-address {
    left: 249px;
    top: 262px;
    font-size: 44px;
  }
  .hashtag {
    left: 300px;
    top: 629px;
    font-size: 44px;
  }
  .icon { position: absolute; }
  .icon-home { left: 24px; top: 441px; width: 88px; height: 74px; }
  .icon-power { left: 249px; top: 449px; width: 96px; height: 71px; }
  .icon-wifi { left: 468px; top: 443px; width: 96px; height: 75px; }
  .icon-phone { left: 677px; top: 416px; width: 78px; height: 124px; }
  .operator {
    position: absolute;
    color: var(--accent);
    font-family: Arial, Helvetica, sans-serif;
    font-weight: 700;
    font-size: 56px;
    line-height: 1;
  }
  .op-plus-1 { left: 133px; top: 478px; }
  .op-plus-2 { left: 384px; top: 476px; }
  .op-plus-3 { left: 596px; top: 474px; }
  .op-equals { left: 810px; top: 476px; }
  .brand {
    position: absolute;
    left: 878px;
    top: 294px;
    width: 315px;
    height: 315px;
    display: flex;
    align-items: center;
    justify-content: center;
  }
  .brand-name {
    margin: 0;
    color: var(--accent);
    font-weight: 700;
    font-size: 40px;
    white-space: nowrap;
  }
</style>
</head>
<body>
<main class="cover">
  <div class="floor-shadow"></div>

  <p class="web-address">www.brightnestwell.com</p>

  <svg class="icon icon-home" viewBox="0 0 88 74" aria-label="Apartment">
    <path d="M44 2 L86 36 L80 42 L74 37 L74 74 L14 74 L14 37 L8 42 L2 36 Z" fill="var(--ink)"/>
    <rect x="62" y="6" width="8" height="18" fill="var(--ink)"/>
    <path d="M36 74 L36 52 Q44 42 52 52 L52 74 Z" fill="#e8e8e8"/>
  </svg>
  <span class="operator op-plus-1">+</span>

  <svg class="icon icon-power" viewBox="0 0 96 71" aria-label="Electricity">
    <path d="M13 28 Q14 58 40 66 Q62 72 80 56 Q86 48 84 38" fill="none" stroke="var(--ink)" stroke-width="1.6"/>
    <circle cx="13" cy="12" r="12" fill="var(--bulb)"/>
    <rect x="7" y="20" width="12" height="9" rx="2" fill="var(--bulb)"/>
    <rect x="8" y="28" width="10" height="4" fill="#333"/>
    <rect x="71" y="2" width="24" height="34" rx="5" fill="var(--ink)"/>
    <circle cx="83" cy="19" r="9" fill="var(--socket)"/>
    <circle cx="80" cy="19" r="1.4" fill="var(--ink)"/>
    <circle cx="86" cy="19" r="1.4" fill="var(--ink)"/>
  </svg>
  <span class="operator op-plus-2">+</span>

  <svg class="icon icon-wifi" viewBox="0 0 96 75" aria-label="Internet">
    <g fill="none" stroke="var(--ink)" stroke-width="8" stroke-linecap="round">
      <path d="M6 26 Q48 -8 90 26"/>
      <path d="M20 40 Q48 16 76 40"/>
      <path d="M34 54 Q48 42 62 54"/>
    </g>
    <circle cx="48" cy="68" r="6" fill="var(--ink)"/>
  </svg>
  <span class="operator op-plus-3">+</span>

  <svg class="icon icon-phone" viewBox="0 0 78 124" aria-label="Mobile connection">
    <rect x="0" y="0" width="78" height="124" rx="9" fill="var(--ink)"/>
    <rect x="7" y="18" width="64" height="84" fill="var(--screen)"/>
    <circle cx="39" cy="113" r="5" fill="var(--screen)"/>
    <path d="M24 48 Q20 52 22 58 Q28 72 42 78 Q48 80 52 76 L54 72 L46 66 L42 70 Q34 66 30 58 L34 54 L28 46 Z" fill="var(--ink)"/>
    <g fill="none" stroke="var(--ink)" stroke-width="2.4" stroke-linecap="round">
      <path d="M44 44 Q52 46 54 54"/>
      <path d="M45 37 Q58 40 61 53"/>
    </g>
  </svg>
  <span class="operator op-equals">=</span>

  <div class="brand">
    <p class="brand-name">Bright Nestwell</p>
  </div>

  <p class="hashtag">#UnpackByDawn</p>
</main>
</body>
</html>
```